RTW Vision and Core Values

We are wanting to promote our core values and vision on posters at our office. I have uploaded a copy of our logo. We would like to incorporate that, the vision and the core values. ALL THREE MUST BE INCLUDED ON THE DESIGN. For reference, our website is www.rtwpetroworks.com

Our vision is:
We are a Team of Power and Strength that Builds our People and Serves our Industry and Communities.

Our Values are:
We Operate with a Standard of Excellence.
We Do the Right Thing Every Time.
We Value and Recognize our People.
We are Team Players.
We Think and Act with Optimism and Faith.

```html
<!DOCTYPE html>
<html lang="en">
<head>
<meta charset="utf-8">
<title>RTW Vision and Core Values</title>
<link href="https://fonts.googleapis.com/css2?family=Red+Hat+Display:wght@400;700&family=Exo+2:wght@800&family=Orbitron:wght@400&display=swap" rel="stylesheet">
<style>
  :root {
    --backdrop: #8a8a8a;
    --poster: #1d1c1c;
    --poster-edge: #232222;
    --ink: #f2f2f2;
    --blue: #2160b8;
    --orange: #e8532a;
    --soft-blue: #2f6fc0;
    --soft-orange: #e2572b;
  }
  * { margin: 0; padding: 0; box-sizing: border-box; }
  html, body {
    width: 998px; height: 1200px; overflow: hidden;
    background: var(--backdrop);
  }
  .poster {
    position: absolute; left: 84px; top: 20px;
    width: 830px; height: 1160px;
    background: radial-gradient(ellipse at 50% 45%, var(--poster-edge), var(--poster) 70%);
    font-family: "Red Hat Display", sans-serif;
    color: var(--ink);
    overflow: hidden;
  }
  .centre-art { position: absolute; left: 200px; top: 170px; width: 420px; height: 710px; }
  .star { position: absolute; left: 352px; top: 106px; width: 86px; height: 86px; }
  .icon { position: absolute; }
  .value-line {
    position: absolute; font-weight: 700; font-size: 24px;
    line-height: 30px; white-space: nowrap; transform: translateY(-15px);
  }
  .align-right { transform: translate(-100%, -15px); }
  .core-values { position: absolute; left: 160px; top: 690px; width: 180px; height: 200px; }
  .vision-title {
    position: absolute; left: 0; width: 100%; top: 885px; text-align: center;
    font-family: "Exo 2", sans-serif; font-weight: 800; font-size: 84px; line-height: 100px;
    letter-spacing: 1px;
  }
  .vision-statement {
    position: absolute; left: 0; width: 100%; top: 978px; text-align: center;
    font-size: 17.5px; line-height: 24px; font-weight: 400;
  }
  .brand {
    position: absolute; left: 48px; top: 1058px;
    font-weight: 700; font-size: 46px; line-height: 56px; color: var(--blue);
    letter-spacing: 2px;
  }
</style>
</head>
<body>
<main class="poster">
  <svg class="centre-art" viewBox="0 0 420 710" role="img" aria-label="Large central flame artwork in blue and orange">
    <defs>
      <radialGradient id="art-glow" cx="50%" cy="55%" r="55%">
        <stop offset="0%" stop-color="var(--soft-orange)" stop-opacity="0.35"/>
        <stop offset="45%" stop-color="var(--soft-blue)" stop-opacity="0.25"/>
        <stop offset="100%" stop-color="var(--soft-blue)" stop-opacity="0"/>
      </radialGradient>
    </defs>
    <ellipse cx="210" cy="380" rx="205" ry="320" fill="url(#art-glow)"/>
  </svg>

  <svg class="star" viewBox="0 0 100 100" aria-hidden="true">
    <polygon points="50,4 61,38 97,38 68,59 79,94 50,73 21,94 32,59 3,38 39,38" fill="var(--ink)"/>
  </svg>

  <svg class="icon" style="left:298px;top:224px;width:58px;height:58px" viewBox="0 0 60 60" aria-hidden="true">
    <circle cx="30" cy="30" r="26" fill="none" stroke="var(--blue)" stroke-width="5"/>
    <polyline points="18,31 27,40 43,22" fill="none" stroke="var(--blue)" stroke-width="5" stroke-linecap="round" stroke-linejoin="round"/>
  </svg>

  <svg class="icon" style="left:516px;top:358px;width:58px;height:58px" viewBox="0 0 60 60" aria-hidden="true">
    <g fill="none" stroke="var(--orange)" stroke-width="4" stroke-linejoin="round">
      <rect x="4" y="26" width="11" height="28" rx="2"/>
      <path d="M15 28 L27 8 Q31 4 33 10 L31 24 H50 Q56 25 55 31 L51 50 Q49 55 44 55 H15"/>
    </g>
  </svg>

  <svg class="icon" style="left:138px;top:456px;width:80px;height:78px" viewBox="0 0 80 78" aria-hidden="true">
    <g fill="none" stroke="var(--orange)" stroke-width="3.5">
      <circle cx="50" cy="18" r="15"/><circle cx="50" cy="14" r="5"/><path d="M41 27 Q50 18 59 27"/>
      <circle cx="18" cy="46" r="15"/><circle cx="18" cy="42" r="5"/><path d="M9 55 Q18 46 27 55"/>
      <circle cx="58" cy="58" r="15"/><circle cx="58" cy="54" r="5"/><path d="M49 67 Q58 58 67 67"/>
      <line x1="38" y1="28" x2="29" y2="36"/><line x1="52" y1="33" x2="55" y2="43"/>
    </g>
  </svg>

  <svg class="icon" style="left:623px;top:592px;width:72px;height:74px" viewBox="0 0 72 74" aria-hidden="true">
    <g fill="none" stroke="var(--blue)" stroke-width="4" stroke-linecap="round" stroke-linejoin="round">
      <path d="M36 4 A24 24 0 0 1 50 48 V54 H22 V48 A24 24 0 0 1 36 4 Z"/>
      <line x1="24" y1="62" x2="48" y2="62"/><line x1="28" y1="70" x2="44" y2="70"/>
      <polyline points="26,27 33,34 46,20"/>
    </g>
  </svg>

  <svg class="icon" style="left:157px;top:664px;width:24px;height:26px" viewBox="0 0 24 26" aria-hidden="true">
    <g fill="none" stroke="var(--ink)" stroke-width="2.5" stroke-linejoin="round">
      <polyline points="3,10 12,2 21,10"/><polyline points="3,17 12,9 21,17"/><polyline points="3,24 12,16 21,24"/>
    </g>
  </svg>

  <section class="values">
    <p class="value-line" style="left:435px;top:216px">We Operate</p>
    <p class="value-line" style="left:435px;top:247px">with a Standard</p>
    <p class="value-line" style="left:435px;top:278px">of Excellence.</p>

    <p class="value-line align-right" style="left:343px;top:308px">We Do</p>
    <p class="value-line align-right" style="left:322px;top:339px">the Right</p>
    <p class="value-line align-right" style="left:302px;top:370px">Thing</p>
    <p class="value-line align-right" style="left:282px;top:401px">Every Time</p>

    <p class="value-line" style="left:542px;top:454px">We Value and</p>
    <p class="value-line" style="left:560px;top:486px">Recognize</p>
    <p class="value-line" style="left:577px;top:517px">our People.</p>

    <p class="value-line align-right" style="left:209px;top:565px">We are</p>
    <p class="value-line align-right" style="left:204px;top:596px">Team</p>
    <p class="value-line align-right" style="left:200px;top:627px">Players</p>

    <p class="value-line" style="left:613px;top:707px">We Think</p>
    <p class="value-line" style="left:600px;top:738px">And Act</p>
    <p class="value-line" style="left:588px;top:769px">With Optimism</p>
    <p class="value-line" style="left:575px;top:800px">And Faith</p>
  </section>

  <svg class="core-values" viewBox="0 0 180 200" aria-label="Core Values">
    <defs><path id="core-arc" d="M22 30 Q40 130 135 180"/></defs>
    <text font-family="Orbitron, sans-serif" font-size="27" fill="var(--orange)">
      <textPath href="#core-arc">Core Values</textPath>
    </text>
  </svg>

  <h1 class="vision-title">vision</h1>
  <p class="vision-statement">We are a Team of Power and Strength<br>that Builds our People and Serves our<br>Industry and Communities.</p>

  <p class="brand">RTW</p>
</main>
</body>
</html>
```